Plakat-Design für Cloud-Telefonanlage
Zielgruppe
https://www.veltrano-beispiel.at/festnetz/business/virtuelle-cloud-telefonanlage
Aufgabenstellung
rollup_xxl_200x300 Grafik - siehe Datenblatt
Überschrift groß: Cloud Telefonanlage aus Tirol
Evt. dann die Features aufzählen [?] dazu hätte ich den Text u. die
Grafik im Anhang 'Cloud-Features' beigefügt.
**** Änderung am 17.06 **** : Die Features nur benennen, sprich ohne Beschreibung! Wird dann zu viel Inhalt.
Hinzufügen:
Computer Telefon Integration (CTI)
Konferenzen
Smartphone App
Sprachaufzeichnungen
Fax2Mail - Mail2Fax
Farbcode: A46CA0

```html
<!DOCTYPE html>
<html lang="de">
<head>
<meta charset="utf-8">
<title>Veltrano – Cloud Telefonanlage Roll-up</title>
<link href="https://fonts.googleapis.com/css2?family=Montserrat:ital,wght@0,300;0,400;0,600;0,700;1,500&family=Nunito:wght@700&display=swap" rel="stylesheet">
<style>
  :root {
    --brand: #a46ca0;
    --icon: #9c6898;
    --ink: #2e2e30;
    --label: #333236;
    --stage: #9aa1ad;
    --sheet-top: #f1f0f1;
    --sheet-mid: #e4dee4;
    --sheet-bottom: #cbb6ca;
  }
  * { margin: 0; padding: 0; box-sizing: border-box; }
  html, body { width: 768px; height: 1200px; overflow: hidden; }
  body { background: var(--stage); position: relative; }

  .rollup {
    position: absolute; left: 104px; top: 0;
    width: 560px; height: 1200px; overflow: hidden;
    background: linear-gradient(180deg, var(--sheet-top) 0%, var(--sheet-mid) 50%, var(--sheet-bottom) 100%);
  }
  .soft-shape {
    position: absolute; border-radius: 50%;
    background: rgba(255,255,255,0.28);
  }
  .soft-shape--top { width: 420px; height: 700px; right: -120px; top: -60px; }
  .soft-shape--mid { width: 300px; height: 420px; left: -140px; top: 380px; }

  .brand {
    position: absolute; right: 58px; top: 110px;
    display: flex; align-items: center; gap: 8px;
    font-family: "Montserrat", sans-serif; font-weight: 600;
    font-size: 30px; color: var(--ink); letter-spacing: 0.5px;
  }
  .brand__square { width: 12px; height: 12px; background: var(--brand); }

  .headline {
    position: absolute; left: 26px; top: 172px;
    font-family: "Montserrat", sans-serif; color: var(--ink); line-height: 1;
  }
  .headline__light { display: block; font-weight: 300; font-size: 34px; letter-spacing: 2px; }
  .headline__bold { display: block; font-weight: 700; font-size: 38px; letter-spacing: 2px; margin-top: 8px; }

  .origin-rule {
    position: absolute; left: 0; top: 268px; width: 252px; height: 2px;
    background: var(--brand);
  }
  .origin {
    position: absolute; left: 264px; top: 259px;
    font-family: "Montserrat", sans-serif; font-style: italic; font-weight: 500;
    font-size: 14px; color: var(--brand);
  }

  .features { position: absolute; left: 0; top: 350px; width: 560px; height: 800px; }
  .feature {
    position: absolute; width: 250px; transform: translateX(-50%);
    display: flex; flex-direction: column; align-items: center; gap: 8px;
    font-family: "Nunito", sans-serif; font-weight: 700; font-size: 12.5px; color: var(--label);
    text-align: center; white-space: nowrap;
  }
  .feature svg { width: 26px; height: 26px; fill: var(--icon); }
  .feature--left { left: 132px; }
  .feature--right { left: 408px; }
</style>
</head>
<body>
<main class="rollup">
  <div class="soft-shape soft-shape--top"></div>
  <div class="soft-shape soft-shape--mid"></div>

  <div class="brand"><span class="brand__name">Veltrano</span><span class="brand__square"></span></div>

  <h1 class="headline">
    <span class="headline__light">CLOUD</span>
    <span class="headline__bold">TELEFONANLAGE</span>
  </h1>
  <div class="origin-rule"></div>
  <p class="origin">AUS TIROL</p>

  <section class="features">
    <!-- left column -->
    <div class="feature feature--left" style="top:0">
      <svg viewBox="0 0 24 24"><path d="M6.6 2.5l3 3.5-1.8 2.6a13 13 0 0 0 7.6 7.6l2.6-1.8 3.5 3-1.7 3.3C11 20.8 3.2 13 2.9 4.2z"/></svg>
      <span>Telefoniefunktion</span>
    </div>
    <div class="feature feature--left" style="top:86px">
      <svg viewBox="0 0 24 24"><path d="M9 4H5a2 2 0 0 0-2 2v12a2 2 0 0 0 2 2h4v-3H6V7h3zm5 1v4H8v6h6v4l8-7z"/></svg>
      <span>Routing &amp; Weiterleitungen</span>
    </div>
    <div class="feature feature--left" style="top:172px">
      <svg viewBox="0 0 24 24"><circle cx="12" cy="7" r="3.5"/><circle cx="5" cy="9" r="2.5"/><circle cx="19" cy="9" r="2.5"/><path d="M6 19a6 6 0 0 1 12 0zM1 17a4 4 0 0 1 5-3.5A7 7 0 0 0 4.5 17zm22 0h-3.5a7 7 0 0 0-1.5-3.5A4 4 0 0 1 23 17z"/></svg>
      <span>Anrufgruppen</span>
    </div>
    <div class="feature feature--left" style="top:258px">
      <svg viewBox="0 0 24 24"><path d="M20 3v16l-8-4H9l1 5H6l-1-5H3V8h9zm-2 3.2L12.5 10H5v3h7.5l5.5 3z"/></svg>
      <span>Ansagen</span>
    </div>
    <div class="feature feature--left" style="top:344px">
      <svg viewBox="0 0 24 24"><path d="M6 5h12l4 8v6H2v-6zm1.4 2L4.5 12H9l1 2h4l1-2h4.5l-2.9-5z"/></svg>
      <span>Virtuelle Sprachbox (Voice2Mail)</span>
    </div>
    <div class="feature feature--left" style="top:430px">
      <svg viewBox="0 0 24 24"><path d="M3 3l18 18-1.6 1.6L1.4 4.6z"/><path d="M6 3l3 3.5-1.5 2 6.5 6.5 2-1.5 3.5 3-1.8 3.5C10 19 5 14 2.6 4.6z"/></svg>
      <span>Verpasste Anrufe &amp; Logs</span>
    </div>
    <div class="feature feature--left" style="top:516px">
      <svg viewBox="0 0 24 24"><path d="M2 3h20v13H13v3h4v2H7v-2h4v-3H2zm2 2v9h16V5z"/><path d="M9 6.5l1.5 1.8-.8 1a6 6 0 0 0 2.8 2.8l1-.8 1.8 1.5-1 1.4C10 13.8 7.2 11 7.6 7.5z"/></svg>
      <span>Computer Telefon Integration (CTI)</span>
    </div>
    <div class="feature feature--left" style="top:602px">
      <svg viewBox="0 0 24 24"><path d="M7 2h10a2 2 0 0 1 2 2v16a2 2 0 0 1-2 2H7a2 2 0 0 1-2-2V4a2 2 0 0 1 2-2zm0 3v13h10V5zm5 14.2a1 1 0 1 0 0 .1z"/></svg>
      <span>Smartphone App</span>
    </div>
    <div class="feature feature--left" style="top:688px">
      <svg viewBox="0 0 24 24"><path d="M2 5h20v14H2zm2 2.4V17h16V7.4l-8 5.6z"/><path d="M4.5 7h15L12 12.2z"/></svg>
      <span>Fax2Mail – Mail2Fax</span>
    </div>

    <!-- right column -->
    <div class="feature feature--right" style="top:12px">
      <svg viewBox="0 0 24 24"><path d="M9 2h6v5h-2v3h7v4h2v5h-6v-5h2v-2H6v2h2v5H2v-5h2v-4h7V7H9zm2 2v1h2V4zM4 16v1h2v-1zm14 0v1h2v-1z"/></svg>
      <span>Durchwahlen Verwaltung</span>
    </div>
    <div class="feature feature--right" style="top:98px">
      <svg viewBox="0 0 24 24"><path d="M12 2a10 10 0 1 0 0 20 10 10 0 0 0 0-20zm-1 4h2v6l3 3-1.4 1.4L11 13z"/></svg>
      <span>Geschäftszeiten</span>
    </div>
    <div class="feature feature--right" style="top:184px">
      <svg viewBox="0 0 24 24"><path d="M3 4h18v3H3zm0 6.5h18v3H3zM3 17h18v3H3z"/></svg>
      <span>IVR-Menü</span>
    </div>
    <div class="feature feature--right" style="top:270px">
      <svg viewBox="0 0 24 24"><path d="M7 10V7a5 5 0 0 1 10 0v3h2v12H5V10zm2.5 0h5V7a2.5 2.5 0 0 0-5 0z"/></svg>
      <span>Anrufsperren &amp; Gesprächslimit</span>
    </div>
    <div class="feature feature--right" style="top:356px">
      <svg viewBox="0 0 24 24"><path d="M4 2h14v20H4zm15 3h2v3h-2zm0 5h2v3h-2zm0 5h2v3h-2zM11 6.5a2.5 2.5 0 1 0 0 5 2.5 2.5 0 0 0 0-5zM7 17h8c0-2.5-1.8-4-4-4s-4 1.5-4 4z"/></svg>
      <span>Globales Telefonbuch</span>
    </div>
    <div class="feature feature--right" style="top:442px">
      <svg viewBox="0 0 24 24"><path d="M2 2h2.5v17.5H22V22H2zm5 10h2.5v5H7zm4-4h2.5v9H11zm4 2h2.5v7H15zm4-5h2.5v12H19z"/></svg>
      <span>Anrufstatistiken</span>
    </div>
    <div class="feature feature--right" style="top:528px">
      <svg viewBox="0 0 24 24"><path d="M2 3h13v9H7l-4 3V12H2zm9 10h4a2 2 0 0 0 2-2V7h5v9h-1v3l-4-3h-6z"/></svg>
      <span>Konferenzen</span>
    </div>
    <div class="feature feature--right" style="top:614px">
      <svg viewBox="0 0 24 24"><path d="M12 2a3.5 3.5 0 0 1 3.5 3.5v6a3.5 3.5 0 0 1-7 0v-6A3.5 3.5 0 0 1 12 2z"/><path d="M5 11h2a5 5 0 0 0 10 0h2a7 7 0 0 1-6 6.9V20h3v2H8v-2h3v-2.1A7 7 0 0 1 5 11z"/></svg>
      <span>Sprachaufzeichnungen</span>
    </div>
  </section>
</main>
</body>
</html>
```